Las Vegas Themed Video & Messaging Zelpad App

We have designed an Zelpad app that allows people to share videos and message one another while visiting Las Vegas, Nevada. However, without a simple, compelling design this app will be "just like the rest". This is where you come in.

As a version 1.0 of this app, we want to test the market as inexpensively as possible. There are other screens that we will need to be designed; during development we will be coming back to you for further iterations and enhancements. Consider this contest a paid interview, in other words.

This app will be available to users in the Quorvo Apps Mart. A mockup is attached to the Files section of this brief.

Our mockup is intentionally devoid of almost all styling because we did not want to get in front of your design. The attached mockup exists only to give you a general guide towards the "feel" of the app, but the elements themselves and their placements can (and should) be freely changed by you.

Please be creative; we're excited to see your work!

Requirements
Must have
• Simplicity is the focus. We'd like to see only a few screens from you to judge your work:

• The home screen.
• The messaging screen.
• A screen that records a video.

Nice to have
• A clean, contemporary design:

• Beautiful typography.
• A "flat-ish" design, avoiding skeuomorphism.

```html
<!DOCTYPE html>
<html lang="en">
<head>
<meta charset="utf-8">
<title>Las Vegas Video &amp; Messaging App – Screens</title>
<link rel="stylesheet" href="https://fonts.googleapis.com/css2?family=Roboto:wght@400;500;700&display=swap">
<style>
  :root {
    --canvas: #ffffff;
    --green: #1f8a3c;
    --green-dark: #0f5e25;
    --green-light: #3fae4f;
    --navy: #0d1a33;
    --navy-deep: #070e1e;
    --red: #b3151d;
    --red-dark: #7d0c12;
    --tab-dark: #1e1e1e;
    --yellow: #ffe13a;
    --tag: #4fb4e8;
    --white: #ffffff;
    --pink: #ff6fb7;
    --cyan: #5fc8ff;
    --key: #fbfbfb;
    --key-dark: #a9b0bc;
    --kbd-bg: #a3a9b5;
    --bar-grey: #8e96a3;
  }
  * { box-sizing: border-box; margin: 0; padding: 0; }
  html, body { width: 1200px; height: 1200px; overflow: hidden; background: var(--canvas); }
  body { position: relative; font-family: "Roboto", Arial, sans-serif; }

  .screen {
    position: absolute; top: 280px; width: 280px; height: 495px;
    transform: scale(1.0909); transform-origin: top left;
    overflow: hidden; background: var(--navy);
  }
  .screen--home { left: 73px; }
  .screen--record { left: 449px; }
  .screen--chat { left: 832px; }

  /* header */
  .app-header {
    position: absolute; top: 0; left: 0; right: 0; height: 52px;
    background: linear-gradient(var(--green-light), var(--green) 55%, var(--green-dark));
    color: var(--white); display: flex; align-items: center;
  }
  .coin-count { position: absolute; left: 9px; top: 15px; display: flex; align-items: center; gap: 6px; font-weight: 700; font-size: 16px; }
  .coin-mark { width: 17px; height: 17px; background: var(--yellow); border-radius: 2px; }
  .app-header__title { width: 100%; text-align: center; font-weight: 700; font-size: 17px; }
  .app-header__add { position: absolute; right: 12px; top: 11px; font-size: 24px; font-weight: 700; line-height: 1; }
  .avatar { position: absolute; right: 8px; top: 8px; width: 35px; height: 35px; border: 1px solid var(--white); background: linear-gradient(#d4553f, #9e2a1e); }

  /* home */
  .search-band {
    position: absolute; top: 52px; left: 0; right: 0; height: 28px;
    background: repeating-linear-gradient(90deg, var(--red-dark) 0 9px, #1a0608 9px 18px);
  }
  .search-field {
    position: absolute; top: 7px; left: 36px; width: 200px; height: 15px; border-radius: 8px;
    background: var(--white); color: #8a8a8a; font-size: 8px; text-align: center; line-height: 15px;
  }
  .feed { position: absolute; top: 80px; left: 0; right: 0; height: 350px; background: radial-gradient(circle at 50% 95%, #1f3466, var(--navy) 55%, var(--navy-deep)); }
  .video-card { position: absolute; width: 116px; }
  .video-card__thumb { position: relative; height: 80px; border: 1px solid #c9ccd4; }
  .video-card__time { position: absolute; right: 4px; bottom: 2px; color: var(--white); font-size: 7px; }
  .video-card__name { margin-top: 5px; color: var(--yellow); font-weight: 700; font-size: 10px; }
  .video-card__by { color: var(--white); font-size: 5px; }
  .video-card__meta { display: flex; justify-content: space-between; color: var(--white); font-size: 7px; margin-top: 1px; }
  .video-card__meta span:last-child { font-size: 6px; }
  .tags { display: flex; gap: 3px; margin-top: 3px; }
  .tag { background: var(--tag); color: var(--white); font-size: 5.5px; font-weight: 700; border-radius: 3px; padding: 1px 4px; }
  .thumb--party { background: linear-gradient(135deg, #7a5a4e, #3c2a26); }
  .thumb--pool { background: linear-gradient(135deg, #b73c3a, #5a8fb6); }
  .thumb--strip { background: linear-gradient(#1b2340, #c88a2c 80%, #5a3010); }
  .thumb--food { background: linear-gradient(135deg, #c26b3c, #8a7a6a); }
  .edge-peek { position: absolute; right: 0; width: 4px; height: 80px; background: #6e6a72; }
  .sign-art {
    position: absolute; left: 60px; top: 262px; width: 160px; height: 86px;
    background: radial-gradient(ellipse at 50% 55%, rgba(230,220,220,.45), rgba(170,50,60,.3) 45%, rgba(13,26,51,0) 72%);
  }

  .tab-bar { position: absolute; top: 430px; left: 0; right: 0; height: 65px; border-top: 5px solid #d9d9d9; display: flex; }
  .tab { flex: 1; display: flex; flex-direction: column; align-items: center; justify-content: flex-end; padding-bottom: 6px; gap: 6px; color: var(--white); font-size: 7.5px; font-weight: 500; background: var(--tab-dark); }
  .tab--red { background: linear-gradient(var(--red), var(--red-dark)); }
  .tab svg { width: 30px; height: 28px; }

  /* record */
  .viewfinder { position: absolute; top: 0; left: 0; right: 0; height: 428px; background: linear-gradient(#4a4f7c, #7a6488 30%, #b97c84 58%, #c9846e 70%, #3a2a2c 85%, #1a1416); }
  .rec { position: absolute; left: 10px; top: 9px; color: var(--white); font-size: 7px; font-weight: 700; display: flex; align-items: center; gap: 3px; }
  .rec::before { content: ""; width: 6px; height: 6px; border-radius: 50%; background: #e0161e; }
  .pill { position: absolute; top: 9px; height: 28px; border-radius: 14px; background: linear-gradient(#c6cfe4, #8993b2); border: 1px solid #5a6180; color: #1d2440; font-size: 13px; font-weight: 500; display: flex; align-items: center; justify-content: center; }
  .pill--options { left: 106px; width: 76px; }
  .pill--flip { left: 212px; width: 60px; }
  .focus-frame { position: absolute; left: 57px; top: 85px; width: 184px; height: 247px; border: 1px solid rgba(255,255,255,.7); }
  .timer { position: absolute; right: 14px; top: 404px; color: var(--white); font-size: 12px; font-weight: 700; }
  .record-band { position: absolute; top: 428px; left: 0; right: 0; height: 7px; background: repeating-linear-gradient(90deg, var(--red) 0 12px, #1a1a1a 12px 18px); }
  .record-bar { position: absolute; top: 435px; left: 0; right: 0; height: 60px; background: linear-gradient(var(--green-light), var(--green-dark)); }
  .last-clip { position: absolute; left: 12px; top: 12px; width: 46px; height: 32px; background: linear-gradient(#3a3f6a, #b4764a); border: 1px solid #ddd; }
  .shutter { position: absolute; left: 119px; top: 7px; width: 45px; height: 45px; border-radius: 50%; background: radial-gradient(circle, #f0f0f0, #8a8a8a); display: flex; align-items: center; justify-content: center; }
  .shutter::after { content: ""; width: 20px; height: 20px; border-radius: 50%; background: radial-gradient(circle at 40% 35%, #ff5a5a, #b00e14); }

  /* chat */
  .chat-area { position: absolute; top: 52px; left: 0; right: 0; height: 206px; background: radial-gradient(ellipse at 50% 30%, #3c3226, #15120f 75%); }
  .message { position: absolute; left: 14px; right: 10px; display: flex; gap: 12px; font-size: 12px; }
  .message__user { width: 58px; flex: none; color: var(--white); font-size: 9px; font-weight: 700; padding-top: 2px; }
  .message__text--pink { color: var(--pink); }
  .message__text--cyan { color: var(--cyan); line-height: 1.2; }
  .composer { position: absolute; top: 258px; left: 0; right: 0; height: 57px; background: linear-gradient(#c8ccd4, var(--bar-grey)); }
  .composer__add { position: absolute; left: 12px; top: 14px; color: #5d6470; font-size: 22px; font-weight: 700; line-height: 1; }
  .composer__field { position: absolute; left: 40px; top: 13px; width: 172px; height: 25px; border-radius: 4px; background: var(--white); color: #9a9a9a; font-size: 13px; padding: 4px 8px; }
  .composer__send { position: absolute; left: 218px; top: 12px; width: 52px; height: 27px; border-radius: 4px; background: linear-gradient(#9aa2ae, #6c7480); color: var(--white); font-size: 13px; font-weight: 500; text-align: center; line-height: 27px; }
  .keyboard { position: absolute; top: 315px; left: 0; right: 0; height: 180px; background: linear-gradient(#c5c9d1, var(--kbd-bg)); padding: 0 2px; }
  .key-row { position: absolute; left: 2px; right: 2px; display: flex; justify-content: center; gap: 5px; }
  .key { height: 36px; width: 23px; border-radius: 4px; background: var(--key); box-shadow: 0 1px 0 #5c6270; display: flex; align-items: center; justify-content: center; font-size: 18px; font-weight: 500; color: #111; }
  .key--dark { background: var(--key-dark); color: var(--white); font-size: 13px; }
  .key--wide { width: 30px; }
</style>
</head>
<body>

<!-- Home screen -->
<section class="screen screen--home">
  <header class="app-header">
    <div class="coin-count"><span class="coin-mark"></span>20</div>
    <div class="app-header__title">App Title</div>
    <div class="app-header__add">+</div>
  </header>
  <div class="search-band"><div class="search-field">Search by username or hashtag</div></div>
  <main class="feed">
    <article class="video-card" style="left:17px;top:8px">
      <div class="video-card__thumb thumb--party" role="img" aria-label="Video still of friends at a party"><span class="video-card__time">12:15</span></div>
      <div class="video-card__name">Video Name</div>
      <div class="video-card__by">Submitted by jason387</div>
      <div class="video-card__meta"><span>2345 views</span><span>1 month ago</span></div>
      <div class="tags"><span class="tag">#Great Party</span><span class="tag">#Free Drinks</span></div>
    </article>
    <article class="video-card" style="left:146px;top:8px">
      <div class="video-card__thumb thumb--pool" role="img" aria-label="Video still of a pool party crowd"><span class="video-card__time">3:56</span></div>
      <div class="video-card__name">Video Name</div>
      <div class="video-card__by">Submitted by jupupop89</div>
      <div class="video-card__meta"><span>2345 views</span><span>1 month ago</span></div>
      <div class="tags"><span class="tag">#Pool Party</span><span class="tag">#Hot Girls</span></div>
    </article>
    <div class="edge-peek" style="top:8px"></div>
    <article class="video-card" style="left:17px;top:148px">
      <div class="video-card__thumb thumb--strip" role="img" aria-label="Video still of the Las Vegas Strip at night"><span class="video-card__time">2:12</span></div>
      <div class="video-card__name">Video Name</div>
      <div class="video-card__by">Submitted by vegasexpert1</div>
      <div class="video-card__meta"><span>2345 views</span><span>1 month ago</span></div>
      <div class="tags"><span class="tag">#TheNight</span><span class="tag">#TheStrip</span></div>
    </article>
    <article class="video-card" style="left:146px;top:148px">
      <div class="video-card__thumb thumb--food" role="img" aria-label="Video still of a seafood buffet"><span class="video-card__time">1:23</span></div>
      <div class="video-card__name">Video Name</div>
      <div class="video-card__by">Submitted by lobsterking</div>
      <div class="video-card__meta"><span>2345 views</span><span>1 month ago</span></div>
      <div class="tags"><span class="tag">#Seafood</span><span class="tag">#AllDayBuffet</span></div>
    </article>
    <div class="edge-peek" style="top:148px"></div>
    <div class="sign-art" role="img" aria-label="Illustration of the Welcome to Las Vegas sign under spotlights"></div>
  </main>
  <nav class="tab-bar">
    <div class="tab">
      <svg viewBox="0 0 30 28"><polygon points="15,1 19,10.5 29,11 21.5,17.5 24,27 15,21.5 6,27 8.5,17.5 1,11 11,10.5" fill="#fff"/></svg>NEWEST</div>
    <div class="tab tab--red">
      <svg viewBox="0 0 30 28"><ellipse cx="15" cy="14" rx="14" ry="9" fill="#fff"/><circle cx="15" cy="14" r="6" fill="#b3151d"/><circle cx="15" cy="14" r="2.5" fill="#fff"/></svg>MOST VIEWS</div>
    <div class="tab">
      <svg viewBox="0 0 30 28"><rect x="1" y="4" width="28" height="20" fill="none" stroke="#fff" stroke-width="2"/><rect x="6" y="9" width="18" height="10" fill="#fff"/><g fill="#fff"><rect x="2" y="5" width="2" height="2"/><rect x="2" y="21" width="2" height="2"/><rect x="26" y="5" width="2" height="2"/><rect x="26" y="21" width="2" height="2"/></g></svg>YOUR VIDEOS</div>
    <div class="tab tab--red">
      <svg viewBox="0 0 30 28"><g fill="#fff"><rect x="1" y="3" width="8" height="9" rx="1"/><rect x="11" y="3" width="8" height="9" rx="1"/><rect x="21" y="3" width="8" height="9" rx="1"/><rect x="1" y="15" width="8" height="9" rx="1"/><rect x="11" y="15" width="8" height="9" rx="1"/><rect x="21" y="15" width="8" height="9" rx="1"/></g></svg>MORE</div>
  </nav>
</section>

<!-- Record screen -->
<section class="screen screen--record">
  <div class="viewfinder" role="img" aria-label="Live camera view of a hotel tower at sunset"></div>
  <div class="rec">REC</div>
  <div class="pill pill--options">Options</div>
  <div class="pill pill--flip">
    <svg width="34" height="18" viewBox="0 0 34 18"><rect x="9" y="4" width="16" height="11" rx="2" fill="#1d2440"/><rect x="13" y="2" width="8" height="3" fill="#1d2440"/><circle cx="17" cy="9.5" r="3.5" fill="#c6cfe4"/><path d="M2 9 a8 6 0 0 1 6 -5" stroke="#1d2440" stroke-width="2" fill="none"/><path d="M32 9 a8 6 0 0 1 -6 5" stroke="#1d2440" stroke-width="2" fill="none"/></svg>
  </div>
  <div class="focus-frame"></div>
  <div class="timer">00:12</div>
  <div class="record-band"></div>
  <div class="record-bar">
    <div class="last-clip" role="img" aria-label="Thumbnail of the last recorded clip"></div>
    <div class="shutter"></div>
  </div>
</section>

<!-- Messaging screen -->
<section class="screen screen--chat">
  <header class="app-header">
    <div class="coin-count"><span class="coin-mark"></span>20</div>
    <div class="app-header__title">Jason668</div>
    <div class="avatar" role="img" aria-label="Profile photo of Jason668"></div>
  </header>
  <div class="chat-area" role="img" aria-label="Photo of a dimly lit bar interior">
    <div class="message" style="top:28px"><span class="message__user">Jamie0909</span><span class="message__text--pink">Nice bar, where is this?</span></div>
    <div class="message" style="top:60px"><span class="message__user">Jason668</span><span class="message__text--cyan">It's between zz ave and xx rd.<br>...right next to KIIOTK.</span></div>
  </div>
  <div class="composer">
    <div class="composer__add">+</div>
    <div class="composer__field">Type your message</div>
    <div class="composer__send">Send</div>
  </div>
  <div class="keyboard">
    <div class="key-row" style="top:6px">
      <span class="key">Q</span><span class="key">W</span><span class="key">E</span><span class="key">R</span><span class="key">T</span><span class="key">Y</span><span class="key">U</span><span class="key">I</span><span class="key">O</span><span class="key">P</span>
    </div>
    <div class="key-row" style="top:51px">
      <span class="key">A</span><span class="key">S</span><span class="key">D</span><span class="key">F</span><span class="key">G</span><span class="key">H</span><span class="key">J</span><span class="key">K</span><span class="key">L</span>
    </div>
    <div class="key-row" style="top:96px">
      <span class="key key--dark key--wide" style="margin-right:8px">⇧</span>
      <span class="key">Z</span><span class="key">X</span><span class="key">C</span><span class="key">V</span><span class="key">B</span><span class="key">N</span><span class="key">M</span>
      <span class="key key--dark key--wide" style="margin-left:8px">⌫</span>
    </div>
    <div class="key-row" style="top:141px">
      <span class="key key--dark" style="width:30px">123</span>
      <span class="key key--dark" style="width:28px">
        <svg width="10" height="16" viewBox="0 0 10 16"><rect x="3" y="1" width="4" height="9" rx="2" fill="#fff"/><path d="M1 7 a4 4 0 0 0 8 0 M5 11 v4" stroke="#fff" stroke-width="1.3" fill="none"/></svg>
      </span>
      <span class="key" style="width:66px;font-size:13px;color:#555">space</span>
      <span class="key" style="width:28px;font-size:15px">@</span>
      <span class="key" style="width:28px">.</span>
      <span class="key key--dark" style="width:66px">return</span>
    </div>
  </div>
</section>

</body>
</html>
```